Asset Mgmt Firm Business Card Design Project

We need a new business card design for our asset management firm. The name of the firm is Meridane CapiLeaf, and the firm is referred to as MCL. We would like to see designs that use blues and greys the business card is to be one-sided. The final design should be conservative to communicate financial safety and growth.

The card must include all of the elements below:

Dominick T. Halvorsen, PhD MBA
Founding Principal

Meridane CapiLeaf Inc
418 Fenwold Street
New York, NY 10482
212-804-3176
dthalvorsen@meridanecapileaf.example
www.meridanecapileaf.example

Our tagline:
"Weighing the risk and return for the next era of life science"

When designing the business card, please abide by Orlanto Press's guidelines here: http://www.orlantopress.example/op/ns/guide/UploadResources.aspx?selectedTab=0?pfid=088&pf_id=088&xnav=DocSpecs#Bleed

Please use Adobe Illustrator or Adobe Photoshop.

This project has now beenĀ guaranteed.

Best Regards,
Nick

Industry/Entity Type

Asset Management

Requirements
Must have
• logo

white background

```html
<!DOCTYPE html>
<html lang="en">
<head>
<meta charset="utf-8">
<title>Meridane CapiLeaf – Business Card Options</title>
<link rel="stylesheet" href="https://fonts.googleapis.com/css2?family=Arimo:wght@400;700&display=swap">
<style>
  :root {
    --navy: #2d2b7c;
    --tint-light: #f1f1f8;
    --tint-mid: #d6d6ea;
    --ink: #3a3a4a;
    --page: #e9e9ec;
    --white: #ffffff;
  }
  * { box-sizing: border-box; margin: 0; padding: 0; }
  html, body {
    width: 764px; height: 1200px; overflow: hidden;
    background: var(--page);
    font-family: "Arimo", Arial, sans-serif;
    color: var(--ink);
  }
  .sheet { position: relative; width: 764px; height: 1200px; }
  .card {
    position: absolute; left: 48px; width: 668px; height: 336px;
    overflow: hidden;
    box-shadow: 0 3px 10px rgba(0,0,0,.25);
  }
  .card--one   { top: 44px;  background: linear-gradient(180deg, var(--tint-light) 0%, var(--tint-mid) 100%); }
  .card--two   { top: 430px; background: var(--white); }
  .card--three { top: 816px; background: linear-gradient(160deg, var(--white) 0%, var(--tint-light) 45%, var(--tint-mid) 100%); }

  .brand { display: flex; align-items: center; gap: 10px; }
  .brand__dot { width: 30px; height: 30px; border-radius: 50%; background: var(--navy); flex: none; }
  .brand__name {
    font-family: "Arimo", Arial, sans-serif; font-weight: 400;
    color: var(--navy); font-size: 50px; letter-spacing: 4px; line-height: 1;
  }
  .tagline { font-size: 14px; color: var(--ink); margin-top: 10px; white-space: nowrap; }
  .person__name { font-size: 19px; color: var(--navy); margin-top: 12px; white-space: nowrap; }
  .person__name .cred { font-size: 11px; }
  .person__role { font-size: 13px; color: var(--ink); margin-top: 2px; }
  .address { font-size: 12.5px; line-height: 1.35; margin-top: 14px; }
  .contacts { font-size: 12.5px; line-height: 1.35; margin-top: 12px; white-space: nowrap; }
  .contacts .label { color: var(--navy); }

  .content { position: absolute; }
  .card--one .content   { left: 28px; top: 22px; }
  .card--two .content   { left: 258px; top: 24px; }
  .card--three .content { left: 28px; top: 24px; }
  .card--three .brand__name { font-size: 58px; }

  .band { position: absolute; left: 0; top: 0; width: 232px; height: 100%; background: var(--navy); }
</style>
</head>
<body>
<main class="sheet">

  <section class="card card--one">
    <div class="content">
      <div class="brand"><span class="brand__dot"></span><span class="brand__name">MCL</span></div>
      <p class="tagline">Weighing the risk and return for the next era of life science</p>
      <p class="person__name">Dominick T. Halvorsen, <span class="cred">PHD MBA</span></p>
      <p class="person__role">Founding Principal</p>
      <p class="address">Meridane CapiLeaf Inc<br>418 Fenwold Street<br>New York, NY 10482</p>
      <p class="contacts"><span class="label">phone:</span> 212-804-3176<br><span class="label">email:</span> dthalvorsen@meridanecapileaf.example<br><span class="label">website:</span> www.meridanecapileaf.example</p>
    </div>
  </section>

  <section class="card card--two">
    <div class="band"></div>
    <div class="content">
      <div class="brand"><span class="brand__dot"></span><span class="brand__name">MCL</span></div>
      <p class="tagline">Weighing the risk and return for the next era of life science</p>
      <p class="person__name">Dominick T. Halvorsen <span class="cred">PHD MBA</span></p>
      <p class="person__role">Founding principal</p>
      <p class="address">Meridane CapiLeaf Inc<br>418 Fenwold Street<br>New York, NY 10482</p>
      <p class="contacts"><span class="label">phone:</span> 212-804-3176<br><span class="label">email:</span> dthalvorsen@meridanecapileaf.example<br><span class="label">website:</span> www.meridanecapileaf.example</p>
    </div>
  </section>

  <section class="card card--three">
    <div class="content">
      <div class="brand"><span class="brand__dot"></span><span class="brand__name">MCL</span></div>
      <p class="tagline">Weighing the risk and return for the next era of life science</p>
      <p class="person__name">Dominick T. Halvorsen <span class="cred">PHD MBA</span></p>
      <p class="person__role">Founding principal</p>
      <p class="address">Meridane CapiLeaf Inc<br>418 Fenwold Street<br>New York, NY 10482</p>
      <p class="contacts"><span class="label">phone:</span> 212-804-3176<br><span class="label">email:</span> dthalvorsen@meridanecapileaf.example<br><span class="label">website:</span> www.meridanecapileaf.example</p>
    </div>
  </section>

</main>
</body>
</html>
```